Children friendly theme required for simple Maths mobile app

Simply the app presents 100 random maths questions one-by-one that the child attempts to answer within a set time.

The title of the app is "Tally Quest Zoom"

See attached mock-up for further details.

Design elements required:

1. Color scheme: Reasonably colorful.

2. Logo: A stylized clock (with a single sweeping (blurred) hand or “alarm clock” style) with the plus, minus, divide and multiplication symbols and numbers spinning around it. The clock is the largest element with the operator symbols smaller and the number small again (numbers can be a mix of sizes). Logo should have square dimensions and needs to scale as large as 512px square and as small as 29px square. No words should be on the icon.

3. Background: All screens will have a common background containing all or parts of the logo in various sizes and positions. If time permits each screen can have a subtle variation of design (e.g.: slight color change etc).

4. Button with simple down-state. In the mock-up navigation buttons have greater-than/less-than symbols to imply direction/flow. This could instead be included in the button design (e.g.: button outline points more to the left or right). “For Parents” IS a button and will be rendered as text only.

5. Splash screen: Can just contain the title, logo and background.

6. Font: The app uses static and dynamic text so the font(s) used will need to be embedded in the app. I was considering using Comic Sans for the text (including the number keypad).

7. Graphics: The app uses two icons - a “star” and “clock” images/icons to indicate the top score and time-limit respectively for participants. The clock icon probably needs to be the same as the clock image in the logo (although this is not essential).

Important: Design needs to be children friendly but plain as visuals are not the focus.

Screen size will be 320 x 480, portrait only.

Files need to be submitted in 32-bit PNG format.

This is my first time using PixelBazaar and my first time formally specifying a design so please ask questions if anything is unclear.
Updates

Hi all,

Budget has been doubled based on advice from PixelBazaar and feedback from some potential designers.

Regards,
   Gareth

Hi all,

Sorry about a late change in the brief - the title of the app is now "Tally Quest Zoom".

Kind regards,
   Gareth

Target Market(s)

Parent/Teachers (but for children to use) – i.e.: This app will unlikely be discovered/downloaded by children.

Requirements
Nice to have
• Slightly different background for each screen. Screens are numbered 1 to 6 in the mockup.
Should not have
• "Overwhelming" or overpowering visuals. The task/content is the focus.

```html
<!DOCTYPE html>
<html lang="en">
<head>
<meta charset="utf-8">
<title>Tally Quest Zoom – App Screens</title>
<link href="https://fonts.googleapis.com/css2?family=Comic+Neue:wght@400;700&display=swap" rel="stylesheet">
<style>
  :root {
    --page-bg: #f2f2f2;
    --frame-yellow: #fff200;
    --screen-blue: #0a64ec;
    --screen-blue-deep: #0537b8;
    --screen-blue-light: #3fa3ff;
    --screen-cyan: #7fd0ff;
    --button-white: #ffffff;
    --ink: #141414;
    --text-white: #ffffff;
    --clock-orange: #f26a1b;
    --clock-cream: #fff3e6;
  }
  * { box-sizing: border-box; margin: 0; padding: 0; }
  html, body {
    width: 1200px; height: 900px; overflow: hidden;
    background: var(--page-bg);
    font-family: "Comic Neue", "Comic Sans MS", cursive;
  }
  .canvas { position: relative; width: 1200px; height: 900px; }

  .screen-frame {
    position: absolute; top: 205px;
    width: 330px; height: 490px;
    background: var(--frame-yellow);
    padding: 24px;
  }
  .screen-frame--splash { left: 210px; }
  .screen-frame--menu { left: 652px; }

  .screen {
    position: relative; width: 100%; height: 100%;
    background: var(--screen-blue);
    overflow: hidden;
  }

  /* Splash */
  .splash-backdrop {
    position: absolute; inset: 0;
    background:
      radial-gradient(ellipse 70% 45% at 50% 62%, rgba(127,208,255,0.55) 0%, rgba(63,163,255,0.25) 45%, rgba(10,100,236,0) 75%),
      linear-gradient(180deg, var(--screen-blue) 0%, #1a7cf5 50%, var(--screen-blue-deep) 100%);
  }
  .splash-title {
    position: absolute; left: 0; right: 0; top: 132px;
    text-align: center; white-space: nowrap;
    font-size: 36px; font-weight: 700; line-height: 1;
    color: var(--ink);
  }
  .splash-emblem {
    position: absolute; left: 66px; top: 198px;
    width: 160px; height: 140px;
    border-radius: 40px;
    background: linear-gradient(160deg, var(--clock-cream) 0%, #ffc89a 45%, var(--clock-orange) 100%);
  }

  /* Menu */
  .menu-title {
    position: absolute; left: 0; right: 0; top: 26px;
    text-align: center; white-space: nowrap;
    font-size: 34px; font-weight: 700; line-height: 1;
    color: var(--ink);
  }
  .menu-option { position: absolute; left: 30px; width: 236px; }
  .menu-option--1 { top: 123px; }
  .menu-option--2 { top: 219px; }
  .menu-option--3 { top: 316px; }

  .start-button {
    display: flex; align-items: center; justify-content: center; gap: 14px;
    width: 234px; height: 46px;
    background: var(--button-white);
    border: 5px solid var(--frame-yellow);
    border-radius: 23px;
    font-size: 23px; color: var(--ink);
    letter-spacing: 0.5px;
  }
  .play-arrow { width: 18px; height: 20px; flex: none; }

  .time-limit {
    display: flex; align-items: center; justify-content: flex-end; gap: 8px;
    margin-top: 10px;
    font-size: 13px; font-weight: 700; color: var(--text-white);
  }
  .menu-option--2 .time-limit { margin-right: -12px; }
  .time-limit sup { font-size: 8px; }
  .clock-icon { width: 20px; height: 20px; flex: none; }

  .parents-link {
    position: absolute; left: 96px; top: 410px;
    display: flex; align-items: center; gap: 14px;
    font-size: 20px; font-weight: 700; color: var(--text-white);
    letter-spacing: 0.5px;
  }
  .parents-link .play-arrow { width: 15px; height: 17px; }
</style>
</head>
<body>
<main class="canvas">

  <section class="screen-frame screen-frame--splash" aria-label="Splash screen">
    <div class="screen">
      <div class="splash-backdrop" role="img" aria-label="Blue background with faint rows of numbers and swirling rings"></div>
      <h1 class="splash-title">Tally Quest Zoom</h1>
      <div class="splash-emblem" role="img" aria-label="Orange alarm clock with plus, minus, divide and multiply symbols and numbers around it"></div>
    </div>
  </section>

  <section class="screen-frame screen-frame--menu" aria-label="Menu screen">
    <div class="screen">
      <h2 class="menu-title">Tally Quest Zoom</h2>

      <div class="menu-option menu-option--1">
        <div class="start-button">Quick Start
          <svg class="play-arrow" viewBox="0 0 18 20"><path d="M0 0 L18 10 L0 20 Z" fill="#141414"/></svg>
        </div>
        <div class="time-limit">
          <svg class="clock-icon" viewBox="0 0 20 20"><circle cx="10" cy="10" r="8.5" fill="none" stroke="#fff" stroke-width="1.6"/><path d="M10 4.5 V10 L6.5 12" fill="none" stroke="#fff" stroke-width="1.6" stroke-linecap="round"/></svg>
          5 minutes
        </div>
      </div>

      <div class="menu-option menu-option--2">
        <div class="start-button">Quick Start 2
          <svg class="play-arrow" viewBox="0 0 18 20"><path d="M0 0 L18 10 L0 20 Z" fill="#141414"/></svg>
        </div>
        <div class="time-limit">
          <svg class="clock-icon" viewBox="0 0 20 20"><circle cx="10" cy="10" r="8.5" fill="none" stroke="#fff" stroke-width="1.6"/><path d="M10 4.5 V10 L6.5 12" fill="none" stroke="#fff" stroke-width="1.6" stroke-linecap="round"/></svg>
          <span>6<sup>1/2</sup> minutes</span>
        </div>
      </div>

      <div class="menu-option menu-option--3">
        <div class="start-button">Quick Start 3
          <svg class="play-arrow" viewBox="0 0 18 20"><path d="M0 0 L18 10 L0 20 Z" fill="#141414"/></svg>
        </div>
        <div class="time-limit">
          <svg class="clock-icon" viewBox="0 0 20 20"><circle cx="10" cy="10" r="8.5" fill="none" stroke="#fff" stroke-width="1.6"/><path d="M10 4.5 V10 L6.5 12" fill="none" stroke="#fff" stroke-width="1.6" stroke-linecap="round"/></svg>
          8 minutes
        </div>
      </div>

      <div class="parents-link">For Parents
        <svg class="play-arrow" viewBox="0 0 18 20"><path d="M0 0 L18 10 L0 20 Z" fill="#ffffff"/></svg>
      </div>
    </div>
  </section>

</main>
</body>
</html>
```